Organic Herbs & Spices container

Greek startup company, which cultivate and trade spices and herbs (such as oregano, mint, thyme, sage etc.)

At present we are interested in only the type and shape of packaging which should be made by materials such as paper, cardboard, laminated paper and others based on paper or plastic.

Package size vary from 80g (2.82oz) - 300g (10.58oz). We are going to use the same packing for a variety of products with different information

* Please find attached our logo which should be included in the design.
* There is no company name available at the moment, however a name placeholder should be included.
* include a placeholder for the type of product (sage, oregano, mint, tea etc...).
* Each package should have a place in order to include product details and nutrition facts.

e.g.
xxxx (company name placeholder)
Sage (product type)
product details and nutrition facts.
Updates

Dear designers,first of all, thank you for your proposals. Please find bellow some updates for the project.- It is mandatory to include the logo into the design - Each package should be able to stored vertically - We are looking for one specific package design, please do not submit many variations of a certain package neither colour differentiations Thanks and good luck Added Wednesday, September 28, 2016

Please avoid the use of images. The same package will be used for all the kinds of products (only name and maybe colour will be different among different products. A transparent frame that will show the contents could be used too) Added Wednesday, September 28, 2016

Please find attached logo in EPS format

Our logo is the baseline, any concepts should be based on it. Try to avoid just adding the logo as a small sticker somewhere on the design. Please try to create around it at any way toy like. This could be, to visualize it as a 3D shape or object which can be used as the container of the products.

Reason: We would like to extend the time of the project. We believe that most of the submitted designs do not comply with our requirements.

Reason: We would like to see a bigger variety of ideas

Target Market(s)

Pretty much to anyone over 20 years old worldwide.

Industry/Entity Type

Nutrition

Requirements
Must have
• It should be attractive, easily recognized, simple yet innovative, durable, functional (easy to use) and easy to store.
Should not have
• Project must not include complex or obnoxious shapes and colours.

```html
<!DOCTYPE html>
<html lang="en">
<head>
<meta charset="utf-8">
<title>Leaf &amp; Field – Spice Carton Dieline</title>
<link href="https://fonts.googleapis.com/css2?family=Tenor+Sans&family=Barlow:wght@400;500&display=swap" rel="stylesheet">
<style>
  :root {
    --bg-top: #2b2e32;
    --bg-bottom: #111213;
    --band-black: #050505;
    --key-dark: #0f1011;
    --key-mid: #1f2022;
    --key-edge: #2c2e31;
    --white-band: #ffffff;
    --cut-line: #17678a;
    --fold-line: #17678a;
    --fold-light: #74c8ec;
    --label-grey: #8f9398;
    --brand-grey: #8d9196;
    --flap-grey: #8a8d91;
    --emboss: #34373b;
    --brand-green: #6c9b2c;
    --brand-gold: #e0b92c;
    --herb-dark: #3f5f28;
    --herb-mid: #5d7e3a;
  }
  * { margin: 0; padding: 0; box-sizing: border-box; }
  html, body { width: 921px; height: 1200px; overflow: hidden; }
  body {
    position: relative;
    background: linear-gradient(180deg, var(--bg-top) 0%, #1d1f22 22%, var(--band-black) 38%);
    font-family: "Tenor Sans", sans-serif;
  }
  .lower-field {
    position: absolute; left: 0; top: 846px; width: 921px; height: 354px;
    background: linear-gradient(180deg, #272a2e 0%, #1c1e20 45%, var(--bg-bottom) 100%);
  }
  .product-window {
    position: absolute; left: 0; top: 458px; width: 921px; height: 388px;
    background: var(--white-band);
  }
  .key-band {
    position: absolute; left: 28px; top: 302px; width: 884px; height: 70px;
    background:
      linear-gradient(180deg, var(--key-mid) 0%, var(--key-dark) 50%, var(--key-mid) 100%);
    border-top: 1px solid var(--key-edge);
    border-bottom: 1px solid var(--key-edge);
    box-shadow: inset 0 0 10px rgba(0,0,0,.9), 0 1px 0 rgba(255,255,255,.04);
  }
  .herb-bunch {
    position: absolute; top: 458px; width: 196px; height: 354px;
    border-radius: 30% 30% 48% 48% / 10% 10% 60% 60%;
    background: radial-gradient(ellipse at 50% 35%, var(--herb-mid) 0%, var(--herb-dark) 55%, rgba(63,95,40,0) 100%);
  }
  .panel-label {
    position: absolute; width: 209px; text-align: center;
    color: var(--label-grey);
  }
  .spice-name {
    top: 419px; font-family: "Barlow", sans-serif; font-weight: 500;
    font-size: 15px; letter-spacing: 1px;
  }
  .brand-name {
    top: 862px; font-size: 19px; color: var(--brand-grey); letter-spacing: .5px;
  }
  .net-weight {
    top: 892px; font-size: 11px; color: var(--brand-grey); letter-spacing: 1px;
  }
  .brand-mark {
    position: absolute; top: 312px; width: 209px;
    display: flex; flex-direction: column; align-items: center; gap: 10px;
  }
  .brand-mark .dot {
    width: 46px; height: 46px; border-radius: 50%; background: var(--brand-green);
  }
  .brand-mark .word {
    color: var(--brand-gold); font-size: 18px; letter-spacing: 1.5px;
  }
  .flap-brand {
    position: absolute; left: 58px; top: 82px; width: 209px; text-align: center;
    transform: rotate(180deg); color: var(--flap-grey); font-size: 12px; letter-spacing: 1px;
  }
  .flap-emboss {
    position: absolute; left: 58px; top: 160px; width: 209px; text-align: center;
    transform: rotate(180deg); color: var(--emboss); font-size: 14px; letter-spacing: 1px;
  }
  .dieline { position: absolute; left: 0; top: 0; }
</style>
</head>
<body>
  <div class="lower-field"></div>
  <div class="product-window"></div>
  <div class="key-band" role="img" aria-label="Embossed Greek key meander border running across the carton"></div>

  <div class="herb-bunch" role="img" aria-label="Hanging bunch of fresh thyme" style="left:62px"></div>
  <div class="herb-bunch" role="img" aria-label="Hanging bunch of fresh thyme" style="left:272px"></div>
  <div class="herb-bunch" role="img" aria-label="Hanging bunch of fresh thyme" style="left:481px"></div>
  <div class="herb-bunch" role="img" aria-label="Hanging bunch of fresh thyme" style="left:690px"></div>

  <div class="brand-mark" style="left:64px"><span class="dot"></span><span class="word">LEAF &amp; FIELD</span></div>
  <div class="brand-mark" style="left:477px"><span class="dot"></span><span class="word">LEAF &amp; FIELD</span></div>

  <p class="panel-label spice-name" style="left:267px">NAME OF SPICE</p>
  <p class="panel-label spice-name" style="left:686px">NAME OF SPICE</p>

  <p class="panel-label brand-name" style="left:58px">LEAF &amp; FIELD</p>
  <p class="panel-label net-weight" style="left:58px">2.82OZ</p>
  <p class="panel-label brand-name" style="left:473px">LEAF &amp; FIELD</p>
  <p class="panel-label net-weight" style="left:473px">2.82OZ</p>

  <p class="flap-brand">LEAF &amp; FIELD</p>
  <p class="flap-emboss">LEAF &amp; FIELD</p>

  <svg class="dieline" width="921" height="1200" viewBox="0 0 921 1200" fill="none">
    <g stroke="var(--cut-line)" stroke-width="2">
      <path d="M58 262 V40 Q58 18 80 18 H245 Q267 18 267 40 V220"/>
      <path d="M267 220 H460 L466 240 L474 262 H557"/>
      <path d="M604 262 H688 L694 240 L698 220 H894 V932"/>
      <path d="M58 262 L24 272 V912 L58 932"/>
      <path d="M58 932 H269 L276 946 L280 974 H477"/>
      <path d="M477 932 V1152 Q477 1174 499 1174 H664 Q686 1174 686 1152 V932"/>
      <path d="M686 974 H884 L888 946 L894 932"/>
    </g>
    <g stroke="var(--fold-line)" stroke-width="1.2" stroke-dasharray="5 4">
      <line x1="58" y1="56" x2="267" y2="56"/>
      <line x1="58" y1="262" x2="894" y2="262"/>
      <line x1="58" y1="932" x2="894" y2="932"/>
      <line x1="486" y1="1136" x2="677" y2="1136"/>
      <line x1="58" y1="262" x2="58" y2="458"/>
      <line x1="267" y1="262" x2="267" y2="458"/>
      <line x1="477" y1="262" x2="477" y2="458"/>
      <line x1="686" y1="262" x2="686" y2="458"/>
      <line x1="58" y1="846" x2="58" y2="932"/>
      <line x1="267" y1="846" x2="267" y2="932"/>
      <line x1="477" y1="846" x2="477" y2="932"/>
      <line x1="686" y1="846" x2="686" y2="932"/>
    </g>
    <g stroke="var(--fold-light)" stroke-width="1.2">
      <line x1="24" y1="458" x2="24" y2="846"/>
      <line x1="894" y1="458" x2="894" y2="846"/>
    </g>
    <g stroke="var(--fold-light)" stroke-width="1.2" stroke-dasharray="5 4">
      <line x1="58" y1="458" x2="58" y2="846"/>
      <line x1="267" y1="458" x2="267" y2="846"/>
      <line x1="477" y1="458" x2="477" y2="846"/>
      <line x1="686" y1="458" x2="686" y2="846"/>
    </g>
  </svg>
</body>
</html>
```